New Web Design Project (Blog, Video Blog and Education)

I have a domain www.brightlatticehub.tv I am looking for a website to post blogs and develop a site like https://tinkerandventure.com/ initially blogs then moving into video podcasting as we gain traction. The idea of www.brightlatticehub.tv is that it is about the connection to people, businesses and ideas that change the world.

Target Market(s)

This is a Blog, Podcast site with training material on it targeted at people who want access to connections and simple information on topics they are interested in.

Coding

Coded - Design and coding required

Number of Pages Required

4 page

Font styles to use
Other font styles liked:
• century gothic

Colors
ec1f27
5c5c5c
ffffff

Requirements
Must have
• Really good usability and A nice clean design that looks simple professional and compelling look at, not too busy and clear obvious navigation.
Nice to have
• Magical attraction to visitors.
Should not have
• Clunky design or poor usability

```html
<!DOCTYPE html>
<html lang="en">
<head>
<meta charset="utf-8">
<title>Bright Lattice</title>
<link rel="stylesheet" href="https://fonts.googleapis.com/css2?family=Jost:ital,wght@0,400;0,500;0,600;1,400&family=Questrial&family=Montserrat:wght@700&display=swap">
<style>
:root{
  --red:#ec1f27;
  --slate:#5c5c5c;
  --white:#ffffff;
  --ink:#3a3a3a;
  --muted:#777777;
  --mist:#f5f5f5;
  --rule:#dddddd;
  --mark:#a3a3a3;
}
*{box-sizing:border-box;margin:0;padding:0}
html,body{width:1200px;height:2687px;overflow:hidden;background:var(--white)}
body{position:relative;font-family:"Questrial",sans-serif;color:var(--ink)}
.abs{position:absolute}

/* header */
.site-header{position:absolute;left:0;top:0;width:1200px;height:79px;background:var(--white)}
.brand{left:63px;top:22px;font-family:"Montserrat",sans-serif;font-weight:700;font-size:14px;line-height:17px;letter-spacing:.5px;color:#111;text-align:center;text-transform:uppercase}
.main-nav a{position:absolute;top:32px;font-size:11px;letter-spacing:.6px;color:var(--slate);text-decoration:none;text-transform:uppercase}
.main-nav a.active{color:var(--red)}
.btn-outline{position:absolute;border:1.5px solid var(--red);color:var(--red);font-family:"Jost",sans-serif;font-weight:600;font-size:11px;letter-spacing:1px;text-transform:uppercase;display:flex;align-items:center;justify-content:center;text-decoration:none;background:transparent}

/* hero */
.hero-photo{left:0;top:79px;width:1200px;height:521px;background:linear-gradient(90deg,#1e1f22 0%,#3d3f45 22%,#8a8f97 50%,#c4c4c2 68%,#dad5cf 85%,#9ea3aa 100%)}
.hero-title{left:165px;top:148px;width:420px;font-family:"Jost",sans-serif;font-weight:600;font-size:47px;line-height:57px;color:var(--white);text-transform:uppercase;letter-spacing:.5px}
.hero-lead{left:168px;top:425px;width:420px;font-size:15px;line-height:20px;color:var(--white)}
.hero-cta{left:168px;top:489px;font-family:"Jost",sans-serif;font-weight:600;font-size:10px;letter-spacing:1px;color:var(--white);text-transform:uppercase}

.signup{left:168px;top:541px;width:400px;height:231px;background:var(--slate);box-shadow:0 12px 30px rgba(0,0,0,.18)}
.field{position:absolute;left:40px;width:320px;height:40px;background:var(--white);font-size:11px;color:#aaa;padding:13px 16px}
.btn-send{position:absolute;left:40px;top:152px;width:104px;height:40px;background:var(--red);color:var(--white);font-family:"Jost",sans-serif;font-weight:600;font-size:10px;letter-spacing:1px;display:flex;align-items:center;justify-content:center}

.intro h2{position:absolute;left:632px;top:672px;width:420px;font-family:"Jost",sans-serif;font-weight:500;font-size:24px;line-height:32px;letter-spacing:1.5px;color:var(--ink);text-transform:uppercase}
.intro p{position:absolute;left:632px;top:788px;width:400px;font-size:12.5px;line-height:19px;color:var(--muted)}

/* training */
.training{left:0;top:962px;width:1200px;height:584px;background:var(--mist)}
.section-title{position:absolute;width:1200px;left:0;text-align:center;font-family:"Jost",sans-serif;font-weight:500;font-size:24px;letter-spacing:1.5px;color:var(--ink);text-transform:uppercase}
.card{position:absolute;top:1100px;width:336px;text-align:center}
.card-media{width:336px;height:199px;box-shadow:0 12px 24px rgba(0,0,0,.14)}
.card-date{margin-top:29px;font-family:"Jost",sans-serif;font-weight:600;font-size:10.5px;letter-spacing:.8px;color:var(--red)}
.card-title{margin-top:10px;font-size:14.5px;line-height:23px;color:var(--ink)}
.card-title.linked span{text-decoration:underline;text-underline-offset:3px}

/* podcast */
.podcast h2{position:absolute;left:168px;top:1676px;font-family:"Jost",sans-serif;font-weight:500;font-size:24px;letter-spacing:1.5px;color:var(--ink);text-transform:uppercase}
.podcast p{position:absolute;left:168px;top:1724px;width:390px;font-size:12.5px;line-height:20px;color:var(--muted)}
.video{left:632px;top:1628px;width:400px;height:278px;background:linear-gradient(90deg,#2b2d31 0%,#4a4c51 30%,#9fa4aa 60%,#d7d8d8 100%);box-shadow:0 14px 30px rgba(0,0,0,.2)}

/* featured */
.featured-label{top:1984px;font-size:14px;letter-spacing:1px}
.press{position:absolute;top:2046px;height:46px;display:flex;align-items:center;justify-content:center;font-family:"Jost",sans-serif;font-weight:600;font-size:36px;color:var(--mark);letter-spacing:-.5px}

/* quote */
.quote-band{left:0;top:2171px;width:1200px;height:238px;background:var(--red);color:var(--white);text-align:center}
.quote-band blockquote{position:absolute;left:0;top:72px;width:1200px;font-family:"Jost",sans-serif;font-style:italic;font-size:26px;line-height:30px;letter-spacing:1px}
.quote-band cite{position:absolute;left:0;top:158px;width:1200px;font-style:normal;font-family:"Jost",sans-serif;font-weight:600;font-size:14px;letter-spacing:1px}

/* footer */
.footer-nav{left:168px;top:2486px;font-size:11px;letter-spacing:.6px;color:var(--slate);text-transform:uppercase;white-space:nowrap}
.footer-nav a{color:var(--slate);text-decoration:none}
.footer-nav a.active{color:var(--red)}
.footer-nav .sep{margin:0 11px;color:#999}
.copyright{left:168px;top:2515px;font-size:10.5px;letter-spacing:.6px;color:var(--slate)}
.social{left:833px;top:2492px}

.newsletter{left:0;top:2606px;width:1200px;height:81px;background:#f3f3f3}
.newsletter-line{position:absolute;left:168px;top:21px;width:649px;height:40px;border-top:1px solid #cfcfcf;border-bottom:1px solid #cfcfcf}
.newsletter-text{position:absolute;left:226px;top:35px;font-size:11.5px;color:#b3b3b3}
.btn-subscribe{position:absolute;left:833px;top:21px;width:199px;height:38px;background:var(--slate);color:var(--white);font-family:"Jost",sans-serif;font-weight:600;font-size:10.5px;letter-spacing:1px;display:flex;align-items:center;justify-content:center}
</style>
</head>
<body>

<header class="site-header">
  <div class="abs brand">Bright<br>Lattice</div>
  <nav class="main-nav">
    <a class="active" href="#" style="left:521px">Home</a>
    <a href="#" style="left:595px">About</a>
    <a href="#" style="left:670px">Podcast</a>
    <a href="#" style="left:761px">Blog</a>
    <a href="#" style="left:833px">Resources</a>
    <a href="#" style="left:937px">Contact</a>
  </nav>
  <a class="btn-outline" href="#" style="left:1032px;top:23px;width:104px;height:33px">Training</a>
</header>

<section class="hero">
  <div class="abs hero-photo" role="img" aria-label="Photo of a thoughtful speaker in a suit wearing a headset microphone, hands steepled"></div>
  <h1 class="abs hero-title">Businesses and ideas that change the world?</h1>
  <p class="abs hero-lead">Get training material and simple information<br>on topics you are interested in</p>
  <p class="abs hero-cta">Drop your email below.</p>
  <form class="abs signup">
    <div class="field" style="top:39px">Your Name</div>
    <div class="field" style="top:95px">Email</div>
    <div class="btn-send">SEND</div>
  </form>
</section>

<section class="intro">
  <h2>Lorem ipsum has been the industry's standard dummy text ever</h2>
  <p>Sed ut perspiciatis unde omnis iste natus error sit voluptatem accusantium doloremque laudantium, totam rem aperiam, eaque ipsa quae ab illo inventore veritatis et quasi architecto beatae vitae dicta sunt explicabo. Nemo enim ipsam voluptatem quia voluptas sit.</p>
</section>

<section>
  <div class="abs training"></div>
  <h2 class="section-title" style="top:1034px">Starting an online training:</h2>
  <article class="card" style="left:64px">
    <div class="card-media" role="img" aria-label="Photo of a smiling woman in a group at a networking event" style="background:linear-gradient(90deg,#b9a99a,#d9cfc6 45%,#8fa3bf)"></div>
    <div class="card-date">JAN.12, 2019</div>
    <div class="card-title linked"><span>Lorem Ipsum has been the industry's<br>standard dummy text ever</span></div>
  </article>
  <article class="card" style="left:432px">
    <div class="card-media" role="img" aria-label="Photo of two women laughing together at a table" style="background:linear-gradient(90deg,#8a8070,#c9b9a4 50%,#7d6a58)"></div>
    <div class="card-date">JAN.15, 2019</div>
    <div class="card-title">Lorem Ipsum has been the industry's<br>standard dummy text ever</div>
  </article>
  <article class="card" style="left:800px">
    <div class="card-media" role="img" aria-label="Photo of an audience applauding at a business seminar" style="background:linear-gradient(90deg,#3c3e44,#c9c4c0 50%,#8b7a70)"></div>
    <div class="card-date">JAN.22, 2019</div>
    <div class="card-title">Lorem Ipsum has been the industry's<br>standard dummy text ever</div>
  </article>
  <a class="btn-outline" href="#" style="left:541px;top:1435px;width:118px;height:32px;font-size:10px">Explore all</a>
</section>

<section class="podcast">
  <h2>Podcast - Lorem ipsum</h2>
  <p>Sed ut perspiciatis unde omnis iste natus voluptatem accusantium doloremque laudantium, totam rem aperiam, eaque ipsa quae ab illo inventore</p>
  <a class="btn-outline" href="#" style="left:168px;top:1820px;width:120px;height:30px;font-size:10px">Explore all</a>
  <div class="abs video" role="img" aria-label="Video still of a young man in a suit working at a desk"></div>
  <svg class="abs" style="left:805px;top:1742px" width="48" height="48" viewBox="0 0 48 48" aria-hidden="true">
    <circle cx="24" cy="24" r="20" fill="none" stroke="#ffffff" stroke-width="2.5"/>
    <path d="M19 15 L33 24 L19 33 Z" fill="none" stroke="#ffffff" stroke-width="2.5" stroke-linejoin="round"/>
  </svg>
</section>

<section class="featured">
  <h2 class="section-title featured-label">As featured in:</h2>
  <div class="press" style="left:63px;width:200px">wavecast</div>
  <div class="press" style="left:321px;width:120px">Ventr.</div>
  <div class="press" style="left:499px;width:206px">tradewire</div>
  <div class="press" style="left:758px;width:120px">Ventr.</div>
  <div class="press" style="left:925px;width:211px;font-weight:400;font-family:'Questrial',sans-serif;font-size:34px">inkframer</div>
</section>

<section class="abs quote-band">
  <blockquote>I like my businesses the same way I like my music:<br>fast and independent.</blockquote>
  <cite>– BRIGHT LATTICE</cite>
</section>

<footer>
  <nav class="abs footer-nav">
    <a class="active" href="#">Home</a><span class="sep">I</span><a href="#">About</a><span class="sep">I</span><a href="#">Podcast</a><span class="sep">I</span><a href="#">Blog</a><span class="sep">I</span><a href="#">Resources</a><span class="sep">I</span><a href="#">Contact</a>
  </nav>
  <p class="abs copyright">© 2019 BRIGHT LATTICE.</p>
  <svg class="abs social" width="200" height="30" viewBox="0 0 200 30" aria-label="Social links">
    <circle cx="15" cy="15" r="14" fill="#eeeeee"/>
    <circle cx="57" cy="15" r="14" fill="#eeeeee"/>
    <circle cx="99" cy="15" r="14" fill="#eeeeee"/>
    <circle cx="141" cy="15" r="14" fill="#eeeeee"/>
    <circle cx="183" cy="15" r="14" fill="#eeeeee"/>
  </svg>

  <div class="abs newsletter">
    <div class="newsletter-line"></div>
    <svg class="abs" style="left:168px;top:20px" width="42" height="42" viewBox="0 0 42 42" aria-hidden="true">
      <path d="M21 3 L39 19 L21 39 L3 19 Z" fill="none" stroke="#b5b5b5" stroke-width="1.2"/>
      <path d="M3 19 L21 27 L39 19" fill="none" stroke="#b5b5b5" stroke-width="1.2"/>
    </svg>
    <p class="newsletter-text">It all starts with one simple action. Drop your email.</p>
    <div class="btn-subscribe">SUBSCRIBE NOW!</div>
  </div>
</footer>

</body>
</html>
```